Learning Habits- Teaching and Learning Policy

Hi,

The philosophy behind this Teaching and Learning Policy is to equip young people (Age 16-18) for many challenges that lies ahead. The pace of technological advancement is so great that it is probable that many jobs our students will do in their lifetime do not yet even exist. We realise that we need to help develop our students into effective lifelong learners – meaning that they will:

-Need to be independent whilst also being able to work as a team.
-Need to apply many different strategies to help take on new concepts.
-Reflect on current practice, and improve.

I have attached the file which has the basic designs of the 4 different leaner habits and what they entail. Each habit is colour coordinated, so please keep the colours the same.

Collaboration- Blue (royal blue)
Persevering- Red
Planning- Orange
Reflection- Yellow

I would ideally like the poster to be transferable into a powerpoint too.

Thanking you all so much.

Perla
Updates

Project Deadline Extended Reason: Hi,I am extending this deadline as I will be requesting some changes to the title / slogan.I need the four learning habits have a catchy name which will motivate students.Please send me some suggestions.Thanking you all.Perla Added Monday, March 28, 2016

Target Market(s)

Teachers and students (age 16-18)

Industry/Entity Type

Education

Font styles to use
Other font styles liked:
• Something friendly to kids- where the a is printed like it is written. Similar to century gothic but more friendly.

Requirements
Must have
• Laid out similar to the the website attached. Interesting, motivational yet educational to students in how they can become lifelong learners.
Nice to have
• I should be able to transfer this to a powerpoint from a poster.
• It can be four posters or one depending on the design.
Should not have
• Each Habit must be colour-coordinated:
• Collaboration- Blue (royal blue)
• Persevering- Red
• Planning- Orange
• Reflection- Yellow
• Thank you,

```html
<!DOCTYPE html>
<html lang="en">
<head>
<meta charset="utf-8">
<title>Learning Habits – Teaching and Learning Policy</title>
<link href="https://fonts.googleapis.com/css2?family=Poppins:wght@600&family=Questrial&display=swap" rel="stylesheet">
<style>
  :root {
    --paper: #f2f2f2;
    --ink: #333333;
    --collab-blue: #263dd4;
    --persevere-red: #ff0000;
    --plan-orange: #ff8000;
    --reflect-yellow: #e5dc00;
    --white: #ffffff;
  }
  * { margin: 0; padding: 0; box-sizing: border-box; }
  html, body { width: 869px; height: 1200px; overflow: hidden; background: var(--paper); }
  .poster { position: relative; width: 869px; height: 1200px; background: var(--paper); font-family: "Questrial", sans-serif; color: var(--ink); }
  .poster-title { position: absolute; top: 96px; left: 0; width: 100%; text-align: center; font-family: "Poppins", sans-serif; font-weight: 600; font-size: 35px; line-height: 46px; letter-spacing: 1px; }
  .poster-subtitle, .poster-footer { position: absolute; left: 0; width: 100%; text-align: center; font-size: 29px; line-height: 36px; letter-spacing: 1px; }
  .poster-subtitle { top: 148px; }
  .poster-footer { top: 1086px; }
  .habit { position: absolute; width: 434px; height: 386px; text-align: center; color: var(--white); }
  .habit--collaboration { left: 0; top: 261px; width: 433px; background: var(--collab-blue); }
  .habit--persevering { left: 433px; top: 261px; width: 436px; background: var(--persevere-red); }
  .habit--planning { left: 0; top: 646px; width: 433px; background: var(--plan-orange); }
  .habit--reflection { left: 433px; top: 646px; width: 436px; background: var(--reflect-yellow); color: var(--ink); }
  .habit-art { position: absolute; border-radius: 6px; }
  .habit-name { position: absolute; left: 0; width: 100%; font-family: "Poppins", sans-serif; font-weight: 600; font-size: 26px; line-height: 34px; }
  .habit-traits { position: absolute; left: 0; width: 100%; list-style: none; font-size: 18px; line-height: 22px; letter-spacing: 0.5px; }
  .habit--collaboration .habit-name, .habit--persevering .habit-name { top: 237px; }
  .habit--collaboration .habit-traits, .habit--persevering .habit-traits { top: 276px; }
  .habit--planning .habit-name, .habit--reflection .habit-name { top: 238px; }
  .habit--reflection .habit-name { left: -1px; }
  .habit--planning .habit-traits, .habit--reflection .habit-traits { top: 277px; }
  .habit--persevering .habit-name, .habit--persevering .habit-traits,
  .habit--reflection .habit-name, .habit--reflection .habit-traits { padding-right: 0; left: -1px; }
</style>
</head>
<body>
<main class="poster">
  <h1 class="poster-title">Learning Habits</h1>
  <p class="poster-subtitle">Teaching and Learning Policy</p>

  <section class="habit habit--collaboration">
    <div class="habit-art" role="img" aria-label="Illustration of four people holding up interlocking puzzle pieces" style="left:100px;top:91px;width:210px;height:127px;background:linear-gradient(90deg,#1a1a1a,#ebe5d3,#1a1a1a,#ebe5d3);opacity:.85"></div>
    <h2 class="habit-name">Collaboration</h2>
    <ul class="habit-traits">
      <li>Empathy and Listening</li>
      <li>Interdependence</li>
      <li>Communication</li>
      <li>Questioning</li>
    </ul>
  </section>

  <section class="habit habit--persevering">
    <div class="habit-art" role="img" aria-label="Illustration of a person pushing boulders up a steep slope beneath small clouds" style="left:111px;top:71px;width:214px;height:170px;background:linear-gradient(155deg,#ff4a4a,#3a3a3a)"></div>
    <h2 class="habit-name">Persevering</h2>
    <ul class="habit-traits">
      <li>Managing Distractions</li>
      <li>Meta-Learing</li>
    </ul>
  </section>

  <section class="habit habit--planning">
    <div class="habit-art" role="img" aria-label="Illustration of a clipboard with charts and a clock" style="left:150px;top:84px;width:132px;height:139px;background:linear-gradient(135deg,#ffffff,#f5d34a)"></div>
    <h2 class="habit-name">Planning</h2>
    <ul class="habit-traits">
      <li>Distilling</li>
    </ul>
  </section>

  <section class="habit habit--reflection">
    <div class="habit-art" role="img" aria-label="Illustration of a white thought bubble" style="left:129px;top:102px;width:137px;height:110px;border-radius:50%;background:radial-gradient(circle,#ffffff 60%,#333333)"></div>
    <h2 class="habit-name">Reflection</h2>
    <ul class="habit-traits">
      <li>Monitoring</li>
      <li>Evaluating</li>
    </ul>
  </section>

  <p class="poster-footer">Teaching and Learning Policy</p>
</main>
</body>
</html>
```